Full Stationary
Business Cards & Stationery for Limo Service - Transportation
Business Cards & Stationery for Limo Service
Professional
Glen Harbury / Dale Pronto
President / General Manager
1187 Fenwick Blvd, Suite 300 Des Moines, IA 50317
844.RQT.CARZ
info@vantregocars.example
www.vantregocars.example
I don't want this card to be too cluttered but I want it to look super sharp and modern. I like modern font however I want it to remain similar to the logo and professional as we are handing these cards to operators throughout the United States.
Be creative. I am unsure of the future demand for QR codes. I have attached 3, one for the website, Facebook, and Twitter. Feel free to use them if you wish, however, if there is something new I am unaware of please feel free to use this new technology. As stated earlier, I am unsure how well these work in todays world versus a few years ago. I have used them previously on the backs of business cards and think it looks cool, however if I am mistaken of something different please let me know.

```html
<!DOCTYPE html>
<html lang="en">
<head>
<meta charset="utf-8">
<title>Vantrego Cars – Business Cards</title>
<link rel="stylesheet" href="https://fonts.googleapis.com/css2?family=Montserrat:wght@400;500;600;700&display=swap">
<style>
  :root {
    --backdrop: #1c1c1e;
    --card-white: #fbfbfb;
    --silver-light: #d9d9d9;
    --silver-mid: #a9a9a9;
    --silver-dark: #7b7b7b;
    --ink: #3a3a3a;
    --ink-soft: #6a6a6a;
    --accent-black: #111111;
  }
  * { box-sizing: border-box; margin: 0; padding: 0; }
  html, body {
    width: 1200px; height: 698px; overflow: hidden;
    background: var(--backdrop);
    font-family: "Montserrat", sans-serif;
  }
  .stage { position: relative; width: 1200px; height: 698px; }

  .card {
    position: absolute;
    width: 500px; height: 286px;
    border-radius: 14px;
    background: var(--card-white);
    overflow: hidden;
  }
  .card--front { left: 80px; top: 90px; }
  .card--back  { left: 620px; top: 320px; }

  .brand {
    display: flex; align-items: center; gap: 10px;
    color: var(--ink);
    font-weight: 600;
    letter-spacing: 3px;
    text-transform: uppercase;
    white-space: nowrap;
  }
  .brand__square {
    width: 26px; height: 26px;
    background: var(--ink);
    flex: none;
  }

  /* Front */
  .card--front .brand {
    position: absolute; left: 112px; top: 100px;
    font-size: 26px;
  }
  .card--front .brand__square { width: 40px; height: 40px; }
  .front-web {
    position: absolute; left: 0; right: 0; top: 198px;
    text-align: center;
    font-size: 11px; letter-spacing: 3px;
    color: var(--ink-soft);
  }

  /* Back */
  .back-art { position: absolute; inset: 0; }
  .card--back .brand {
    position: absolute; left: 36px; top: 70px;
    font-size: 15px;
  }
  .person { position: absolute; left: 36px; top: 150px; }
  .person__name {
    font-size: 14px; font-weight: 700; letter-spacing: 1px;
    color: var(--ink); text-transform: uppercase;
  }
  .person__title {
    font-size: 8px; letter-spacing: 2px; color: var(--ink-soft);
    text-transform: uppercase; margin-top: 3px;
  }
  .address {
    position: absolute; left: 36px; top: 232px;
    font-size: 8.5px; line-height: 1.5; color: var(--ink);
  }
  .contacts {
    position: absolute; right: 18px; top: 36px;
    list-style: none;
    font-size: 7.5px; color: #ffffff;
  }
  .contacts li {
    display: flex; align-items: center; justify-content: flex-end;
    gap: 6px; height: 16px; white-space: nowrap;
  }
  .contacts svg { width: 11px; height: 11px; flex: none; }
  .back-web {
    position: absolute; right: 18px; bottom: 14px;
    font-size: 8.5px; color: #ffffff; letter-spacing: 0.5px;
  }
</style>
</head>
<body>
<main class="stage">

  <section class="card card--front" aria-label="Card front">
    <div class="brand"><span class="brand__square"></span>Vantrego Cars</div>
    <p class="front-web">www.vantregocars.example</p>
  </section>

  <section class="card card--back" aria-label="Card back">
    <svg class="back-art" viewBox="0 0 500 286" preserveAspectRatio="none" aria-hidden="true">
      <defs>
        <linearGradient id="silverBand" x1="0" y1="0" x2="1" y2="1">
          <stop offset="0" stop-color="#c4c4c4"/>
          <stop offset="0.5" stop-color="#9c9c9c"/>
          <stop offset="1" stop-color="#7a7a7a"/>
        </linearGradient>
        <linearGradient id="silverStrip" x1="0" y1="0" x2="1" y2="0">
          <stop offset="0" stop-color="#e6e6e6"/>
          <stop offset="1" stop-color="#bdbdbd"/>
        </linearGradient>
      </defs>
      <rect x="0" y="222" width="270" height="64" fill="url(#silverStrip)"/>
      <path d="M270 0 C 370 40, 360 190, 230 286 L 500 286 L 500 0 Z" fill="url(#silverBand)"/>
      <path d="M262 0 C 365 42, 352 190, 220 286" fill="none" stroke="var(--accent-black)" stroke-width="4"/>
      <path d="M270 0 C 370 40, 360 190, 230 286" fill="none" stroke="#ffffff" stroke-width="1.5"/>
    </svg>

    <div class="brand"><span class="brand__square"></span>Vantrego Cars</div>

    <div class="person">
      <p class="person__name">Glen Harbury</p>
      <p class="person__title">President</p>
    </div>

    <p class="address">1187 Fenwick Blvd, Suite 300<br>Des Moines, IA 50317</p>

    <ul class="contacts">
      <li>844.RQT.CARZ
        <svg viewBox="0 0 12 12"><circle cx="6" cy="6" r="6" fill="#fff"/><path d="M4 3.2l1.2 1.4-.6.8c.4.9 1.1 1.6 2 2l.8-.6 1.4 1.2-.8 1c-2.6-.3-4.5-2.2-4.8-4.8z" fill="#8a8a8a"/></svg>
      </li>
      <li>844.RQT.CARS
        <svg viewBox="0 0 12 12"><circle cx="6" cy="6" r="6" fill="#fff"/><rect x="3.3" y="4.2" width="5.4" height="4" fill="#8a8a8a"/></svg>
      </li>
      <li>info@vantregocars.example
        <svg viewBox="0 0 12 12"><circle cx="6" cy="6" r="6" fill="#fff"/><rect x="3" y="4" width="6" height="4.2" fill="none" stroke="#8a8a8a" stroke-width="0.9"/><path d="M3 4l3 2.3L9 4" fill="none" stroke="#8a8a8a" stroke-width="0.9"/></svg>
      </li>
      <li>Des Moines, IA
        <svg viewBox="0 0 12 12"><circle cx="6" cy="6" r="6" fill="#fff"/><path d="M6 2.6a2.2 2.2 0 0 1 2.2 2.2C8.2 6.4 6 9.2 6 9.2S3.8 6.4 3.8 4.8A2.2 2.2 0 0 1 6 2.6z" fill="#8a8a8a"/></svg>
      </li>
    </ul>

    <p class="back-web">www.vantregocars.example</p>
  </section>

</main>
</body>
</html>
```